Flyer-Design für medizinische Ausbildung
Zielgruppe
LOTUS Ausbildung für den qualifizierten Krankentransport und Rettungsdienst in Berlin
Der qualifizierte Krankentransport und Rettungsdienst ist zuständig für den Transport- und Versorgung von kranken und verletzten Menschen. LOTUS Medizinische Ausbildung und Seminare hat sich als Fachschule für die präklinische Notfallmedizin auf Aus- und Weiterbildungen für diese zwei Fachbereiche spezialisiert. Unsere Fachausbildungen orientieren sich streng an gesetzlichen Erfordernissen und realitätsnahen medizinischen Anforderungen.
Aufgabenstellung
Bitte farblich an unsere aktuelle Internetseite orientieren. Bilder & Texte können Sie gerne ebenfalls von unserer Website nutzen. www.notfallkurse-zentrum.example

```html
<!DOCTYPE html>
<html lang="de">
<head>
<meta charset="utf-8">
<title>LOTUS Ausbildung – Flyer</title>
<link href="https://fonts.googleapis.com/css2?family=Roboto+Condensed:wght@500;700&family=Source+Sans+3:wght@400;600;700&display=swap" rel="stylesheet">
<style>
:root{
  --bg:#eceef1;
  --paper:#f5f6f8;
  --blue:#8fb6e1;
  --blue-mid:#7fa6d2;
  --blue-deep:#6e92bd;
  --blue-text:#7ea9da;
  --photo-a:#e4e7ec;
  --photo-b:#c7ccd5;
  --strip:#d9dce1;
  --white:#ffffff;
  --ink:#3d4654;
}
*{box-sizing:border-box;margin:0;padding:0}
html,body{width:1200px;height:900px;overflow:hidden;background:var(--bg)}
body{font-family:"Source Sans 3",Arial,sans-serif;color:var(--white)}
.spread{position:absolute;top:246px;width:575px;height:408px;display:flex;box-shadow:0 18px 30px rgba(0,0,0,.18);background:var(--paper)}
.spread--outside{left:15px}
.spread--inside{left:610px}
.panel{position:relative;width:33.333%;height:100%;overflow:hidden}
.photo{position:absolute;left:0;right:0;top:5%;bottom:0;background:linear-gradient(160deg,var(--photo-a) 0%,#d3d8e0 45%,var(--photo-b) 100%)}
.spread--inside .photo-band{position:absolute;left:0;width:575px;top:4%;height:40%;background:linear-gradient(170deg,var(--photo-a),#cfd4dc 60%,#bfc5cf)}
.shape{position:absolute;inset:0}
.headline{font-family:"Roboto Condensed",Arial,sans-serif;font-weight:700;text-transform:uppercase;letter-spacing:.02em;line-height:1.3}
.copy{font-size:6px;line-height:1.35}

/* outside panel 1 */
.o1 .blue{background:var(--blue);clip-path:polygon(0 20%,100% 3%,100% 80%,0 55%)}
.o1 .lower{background:var(--paper);clip-path:polygon(0 55%,100% 80%,100% 100%,0 100%)}
.rating-badge{position:absolute;left:22px;top:30px;width:110px;height:110px;border-radius:50%;background:var(--white);border:5px solid #e7e9ec;box-shadow:0 2px 6px rgba(0,0,0,.12)}
.o1 .copy{position:absolute;left:14px;right:14px;top:172px;text-align:right}
.o1 .headline{position:absolute;left:14px;top:312px;font-size:13px;color:var(--blue-text)}

/* outside panel 2 */
.o2 .blue{background:var(--blue-mid);clip-path:polygon(0 42%,100% 58%,100% 100%,0 100%)}
.map{position:absolute;left:54px;top:177px;width:78px;height:78px;border-radius:50%;background:linear-gradient(135deg,#f3f4f6,#dde2e8);border:3px solid var(--white)}
.contact{position:absolute;left:0;right:0;top:262px;text-align:center;font-size:7px;font-weight:700;line-height:2.3}
.contact .web{font-size:6px;line-height:1.9;margin-top:4px}

/* outside panel 3 / cover */
.o3 .blue{background:var(--blue-deep);clip-path:polygon(0 58%,100% 79%,100% 100%,0 100%)}
.wordmark{font-family:"Source Sans 3",Arial,sans-serif;font-weight:700;color:var(--white)}
.o3 .wordmark{position:absolute;right:16px;top:44px;font-size:14px;letter-spacing:.06em}
.o3 .headline{position:absolute;left:12px;right:12px;top:312px;font-size:13px;color:#e8edf4}
.o3 .headline .r{display:block;text-align:right}

/* inside spread */
.band{position:absolute;left:0;right:0;top:37%;bottom:8%;background:var(--blue-mid)}
.i1 .strip{position:absolute;left:0;right:0;bottom:0;height:8%;background:var(--strip)}
.i1 .headline{position:absolute;left:18px;top:62px;font-size:13px;color:var(--blue-text)}
.feature{position:absolute;left:18px;right:10px;display:flex;gap:8px;align-items:flex-start}
.feature .ico{flex:0 0 28px;height:28px;border-radius:50%;border:1.3px solid var(--white);display:flex;align-items:center;justify-content:center}
.feature h3{font-size:6.8px;font-weight:700;margin-bottom:1px}
.feature--right{flex-direction:row-reverse}
.cta{position:absolute;left:18px;right:12px;top:340px}
.cta h4{font-size:6.8px;font-weight:700;margin-bottom:8px}

.i2 .band{background:var(--blue)}
.i2 .strip{position:absolute;left:0;right:0;bottom:0;height:8%;background:#e2e5e9}
.person-box{position:absolute;left:14px;top:130px;width:100px;background:var(--white);color:var(--ink);padding:4px 5px;font-size:4.3px;line-height:1.45;text-align:justify}
.person-box strong{display:block;font-size:4.6px;margin-bottom:3px}
.portrait{position:absolute;left:116px;top:122px;width:72px;height:72px;border-radius:50%;border:3px solid var(--white);background:linear-gradient(160deg,#b9c2cf,#5f6a79)}
.i2 .headline{position:absolute;left:16px;top:214px;font-size:11px;line-height:1.55}
.i2 .copy{position:absolute;left:16px;right:16px;top:262px;text-align:justify;font-size:5.6px}
.i2 .wordmark{position:absolute;right:18px;top:330px;font-size:24px;letter-spacing:.08em}
.i2 .foot{position:absolute;left:16px;right:16px;bottom:6px;font-size:3.8px;color:#8a93a0;line-height:1.4}

.i3 .band{top:36%;background:var(--blue)}
.i3 .headline{position:absolute;right:16px;top:94px;font-size:13px;color:var(--blue-text)}
.i3 .title{position:absolute;left:14px;top:160px;font-size:7px;font-weight:700}
.overview-art{position:absolute;left:14px;top:180px;width:164px;height:140px;border-radius:8px;background:linear-gradient(160deg,#c9dcf1,#a9c6e8)}
.courses{position:absolute;left:16px;top:332px;font-size:6.4px;line-height:1.5;list-style:none}
</style>
</head>
<body>

<section class="spread spread--outside">
  <div class="panel o1">
    <div class="photo" role="img" aria-label="Foto eines Einsatzprotokolls auf einem Klemmbrett"></div>
    <div class="shape blue"></div>
    <div class="shape lower"></div>
    <div class="rating-badge" role="img" aria-label="Bewertungsabzeichen"></div>
    <p class="copy">Immer wieder wird gefragt, weshalb die Preise bei LOTUS so moderat sind. Die Antwort ist kurz und knapp beantwortet, wir möchten unsere Ausbildungen Jedem ermöglichen. Speziell die Zielgruppe, die keine Förderungen durch die Arbeitsagenturen in Anspruch nehmen können. Unsere Branche benötigt dringend Nachwuchs. Aufgrund dessen fördern wir auf unsere Art mit fairen Preisen zukünftiges, motiviertes und junges Fachpersonal.</p>
    <h2 class="headline">Unsere unsere<br>Preise sind fair und<br>sozial.</h2>
  </div>
  <div class="panel o2">
    <div class="photo" role="img" aria-label="Foto eines Rettungsdokumentationsbogens"></div>
    <div class="shape blue"></div>
    <div class="map" role="img" aria-label="Kartenausschnitt mit Standort der Schule"></div>
    <div class="contact">
      Lindenweg 12<br>10115 Berlin<br>Tel. + 030 5550124 10<br>Fax +030 5550124 11
      <div class="web">info@notfallkurse-zentrum.example<br>www.notfallkurse-zentrum.example</div>
    </div>
  </div>
  <div class="panel o3">
    <div class="photo" role="img" aria-label="Foto eines Einsatzprotokolls mit Klemmbrett"></div>
    <div class="shape blue"></div>
    <span class="wordmark">LOTUS</span>
    <h1 class="headline">Wir sind<br>für Sie ...<span class="r">... im Einsatz</span></h1>
  </div>
</section>

<section class="spread spread--inside">
  <div class="photo-band" role="img" aria-label="Foto eines Einsatzprotokolls auf einem Klemmbrett"></div>

  <div class="panel i1">
    <h2 class="headline">Für Sie ...</h2>
    <div class="band"></div>
    <div class="feature" style="top:160px">
      <span class="ico"><svg width="14" height="14" viewBox="0 0 14 14" fill="none" stroke="#fff" stroke-width="1"><rect x="1" y="2" width="12" height="8" rx="1"/><path d="M5 13h4M7 10v3"/></svg></span>
      <div class="copy"><h3>Qualifizierte Fachschule</h3>Fachausbildungen streng nach gesetzlichen Erfordernissen und realitätsnahen medizinischen Anforderungen.</div>
    </div>
    <div class="feature feature--right" style="top:214px">
      <span class="ico"><svg width="14" height="14" viewBox="0 0 14 14" fill="none" stroke="#fff" stroke-width="1"><rect x="1" y="1" width="12" height="10" rx="1"/><path d="M4 8l2 2 4-5"/></svg></span>
      <div class="copy"><h3>Medizinische Ausbildung</h3>LOTUS hat sich als Fachschule für die präklinische Notfallmedizin auf Aus- und Weiterbildungen für diese zwei Fachbereiche spezialisiert.</div>
    </div>
    <div class="feature" style="top:274px">
      <span class="ico"><svg width="14" height="14" viewBox="0 0 14 14" fill="none" stroke="#fff" stroke-width="1"><rect x="2" y="1" width="10" height="12" rx="1"/><circle cx="7" cy="8" r="2.5"/><path d="M4 4h6"/></svg></span>
      <div class="copy"><h3>Faire Preise</h3>Unsere Branche benötigt dringend Nachwuchs. Aufgrund dessen fördern wir auf unsere Art mit fairen Preisen zukünftiges, motiviertes und junges Fachpersonal.</div>
    </div>
    <div class="cta copy">
      <h4>Jetzt Ausbildungplatz zum fairen Preis sichern!</h4>
      Näherer Informationen auf unsrere Website oder rufen Sie uns an, wir helfen Ihnen gerne weiter.
    </div>
    <div class="strip"></div>
  </div>

  <div class="panel i2">
    <div class="band"></div>
    <div class="person-box">
      <strong>Ihr Ansprechpartner bei LOTUS</strong>
      Markus Feld ist Rettungsfachkraft aus Leidenschaft und Schulleiter von LOTUS Medizinische Ausbildung u. Seminare. Als Fachausbilder für den qualifizierten Krankentransport ist er Dozent, Mentor und Ansprechpartner, auch nach Abschluss der Ausbildung. Ganz nach dem Motto: „Entweder finden wir einen Weg oder wir machen einen.“
    </div>
    <div class="portrait" role="img" aria-label="Porträtfoto des Schulleiters"></div>
    <h2 class="headline">Warum eine<br>Ausbildung bei LOTUS?</h2>
    <p class="copy">Wir bieten Ihnen eine umfassende Fachausbildung in Form von handlungs- und lernorientiertem Unterricht. Unsere Lehrbeauftragten sind erfahrende Rettungsdienstler, Pflegekräfte und Mediziner mit weitreichender Berufserfahrung. Durch fundierte Fachinhalte, praxisrelevanter Methodik und geschulter Didaktik beschulen und begleiten wir Sie bis zum gewünschten Fachabschluss.</p>
    <span class="wordmark">LOTUS</span>
    <div class="strip"></div>
    <p class="foot">LOTUS Medizinische Ausbildung und Seminare<br>Fachschule für den qualifizierten Krankentransport und Rettungsdienst in Berlin</p>
  </div>

  <div class="panel i3">
    <h2 class="headline">... im Einsatz</h2>
    <div class="band"></div>
    <p class="title">Unsere Ausbildungen im Überblick:</p>
    <div class="overview-art" role="img" aria-label="Illustration der Ausbildungsbereiche rund um die Schule"></div>
    <ul class="courses">
      <li>- Ausbildung zum Transportsanitäter</li>
      <li>- Ausbildung zum Rettungshelfer</li>
      <li>- Ausbildung zum Rettungssanitäter</li>
    </ul>
  </div>
</section>

</body>
</html>
```